Election features for a political website

The Evening Lantern (www.eveninglantern.co.uk)
Web banner designs
Please have a look at The Evening Lantern website (www.eveninglantern.co.uk). We are seeking to add an advertising style banner at the top of every page and post. It will run right across the page (1024 pixels) and be in the region of 200 pixels vertically. (Please advise on what looks best size wise.
The banner will be a slider, operated in a similar way to the current homepage slider. There will be four items on the slider, and so we need four designs that match the aesthetic feel of the website. Each slider will link through to posts on the website.
1.
Headline: OUR CANDIDATE OF THE DAY
Space for a name, head and shoulders picture of the person to be dropped in and a one line reason. This will need to be in an editable format as this image will be changed each day for one month.
2.
Headline: HERO OF THE DAY
Space for name and a one line reason. This will need to be in an editable format as this image will be changed each day for one month.
3.
Headline: VILLAIN OF THE DAY
Space for name of the person to be dropped in and a one line reason. This will need to be in an editable format as this image will be changed each day for one month.
4.
Headline: TEL Poll – [Date]
If the election was today, who would you vote for?
Clickable options:
Harbourites
Meridan
Tallow Assembly
Pomo
Quill
Other
Can a poll widget be added to the banner? We would like this poll to reset each day and then pool the results into a graph day by day over a one month period.
Reason: Payment is now guaranteed. We would like to see more options.

```html
<!DOCTYPE html>
<html lang="en">
<head>
<meta charset="utf-8">
<title>Hero of the Day – The Evening Lantern</title>
<link href="https://fonts.googleapis.com/css2?family=Oswald:wght@400;700&family=Raleway:wght@400&family=Fira+Sans:wght@400&family=Fira+Sans+Condensed:wght@700;800&display=swap" rel="stylesheet">
<style>
  :root {
    --brand-blue: #0b5592;
    --brand-blue-light: #2a6aa3;
    --white: #ffffff;
    --nav-bg: rgba(30, 30, 30, 0.72);
    --panel-bg: rgba(45, 45, 45, 0.42);
    --frame-grey: #5a5f66;
    --search-text: #c9c9c9;
    --tone-deep: #1f1f1f;
    --tone-dark: #3a3a3a;
    --tone-mid: #7a7a7a;
    --tone-light: #c4c4c4;
    --tone-bright: #e6e6e6;
  }
  * { margin: 0; padding: 0; box-sizing: border-box; }
  html, body { width: 1200px; height: 730px; overflow: hidden; background: var(--white); }
  .canvas { position: relative; width: 1200px; height: 730px; overflow: hidden; }

  /* Hero banner */
  .hero-banner {
    position: absolute; left: 0; top: 0; width: 1200px; height: 191px;
    background: var(--brand-blue);
    border-bottom: 1px solid rgba(255,255,255,0.7);
  }
  .banner-backdrop { position: absolute; top: 0; height: 190px; }
  .banner-backdrop--left {
    left: 0; width: 230px;
    background: radial-gradient(ellipse at 40% 40%, var(--brand-blue-light) 0%, var(--brand-blue) 75%);
  }
  .banner-backdrop--right {
    right: 0; width: 260px;
    background: radial-gradient(ellipse at 60% 45%, var(--brand-blue-light) 0%, var(--brand-blue) 75%);
  }
  .banner-title {
    position: absolute; left: 172px; top: 42px;
    font-family: "Oswald", sans-serif; color: var(--white); text-transform: uppercase;
  }
  .banner-title__main { display: block; font-weight: 700; font-size: 64px; line-height: 68px; }
  .banner-title__sub { display: block; margin-left: 63px; margin-top: 0; font-weight: 400; font-size: 31px; line-height: 34px; }
  .hero-portrait {
    position: absolute; left: 409px; top: 21px; width: 145px; height: 146px;
    border: 3px solid var(--frame-grey); border-radius: 6px;
    background: linear-gradient(170deg, #dcd8d4 0%, #b89a80 45%, #8a6a52 70%, #4f6f92 100%);
    box-shadow: 0 0 4px rgba(0,0,0,0.35);
  }
  .hero-name {
    position: absolute; left: 573px; top: 52px;
    font-family: "Oswald", sans-serif; font-weight: 400; font-size: 32px; line-height: 44px; color: var(--white);
  }
  .hero-reason {
    position: absolute; left: 567px; top: 102px;
    font-family: "Raleway", sans-serif; font-size: 15px; color: var(--white);
  }

  /* Site slider */
  .site-slider {
    position: absolute; left: 0; top: 192px; width: 1200px; height: 538px;
    background:
      radial-gradient(ellipse 260px 200px at 640px 150px, rgba(235,235,235,0.85) 0%, rgba(235,235,235,0) 100%),
      radial-gradient(ellipse 220px 170px at 980px 180px, rgba(220,220,220,0.75) 0%, rgba(220,220,220,0) 100%),
      radial-gradient(ellipse 180px 300px at 1110px 420px, rgba(210,210,210,0.55) 0%, rgba(210,210,210,0) 100%),
      radial-gradient(ellipse 140px 260px at 560px 330px, rgba(200,200,200,0.5) 0%, rgba(200,200,200,0) 100%),
      radial-gradient(ellipse 200px 330px at 70px 330px, rgba(20,20,20,0.8) 0%, rgba(20,20,20,0) 100%),
      radial-gradient(ellipse 260px 140px at 880px 530px, rgba(25,25,25,0.7) 0%, rgba(25,25,25,0) 100%),
      linear-gradient(180deg, var(--tone-dark) 0%, var(--tone-light) 22%, var(--tone-mid) 50%, var(--tone-dark) 80%, var(--tone-deep) 100%);
  }
  .site-nav {
    position: absolute; left: 515px; top: 197px; width: 685px; height: 33px;
    background: var(--nav-bg);
    display: flex; align-items: center; padding-left: 36px;
  }
  .site-nav__link {
    font-family: "Fira Sans Condensed", sans-serif; font-weight: 700; font-size: 13.5px;
    color: var(--white); text-decoration: none; margin-right: 13px;
  }
  .site-nav__search {
    margin-left: 3px; font-family: "Fira Sans", sans-serif; font-size: 12.5px; color: var(--search-text);
  }
  .site-brand {
    position: absolute; left: 118px; top: 240px;
    display: flex; align-items: center; gap: 14px;
  }
  .site-brand__mark { width: 26px; height: 26px; background: var(--brand-blue); }
  .site-brand__name {
    font-family: "Fira Sans Condensed", sans-serif; font-weight: 800; font-size: 44px; color: var(--white);
    text-shadow: 0 1px 3px rgba(0,0,0,0.45);
  }
  .slide-panel {
    position: absolute; left: 118px; top: 474px; width: 710px; height: 194px;
    background: var(--panel-bg);
  }
  .slide-headline {
    position: absolute; left: 138px; top: 478px; width: 640px;
    font-family: "Fira Sans Condensed", sans-serif; font-weight: 800; font-size: 38px; line-height: 46px;
    color: var(--white); text-shadow: 0 1px 2px rgba(0,0,0,0.4);
  }
  .slide-arrows { position: absolute; left: 163px; top: 699px; }
</style>
</head>
<body>
<div class="canvas">
  <header class="hero-banner">
    <div class="banner-backdrop banner-backdrop--left" role="img" aria-label="Faint blue-toned photo of a smiling woman"></div>
    <div class="banner-backdrop banner-backdrop--right" role="img" aria-label="Faint blue-toned photo of a laughing woman"></div>
    <h1 class="banner-title">
      <span class="banner-title__main">Hero</span>
      <span class="banner-title__sub">of the day</span>
    </h1>
    <div class="hero-portrait" role="img" aria-label="Head and shoulders photo of today's hero"></div>
    <h2 class="hero-name">John Smith</h2>
    <p class="hero-reason">“ Lorem ipsum dolor sit amet consectetur adipisicing elit ”</p>
  </header>

  <section class="site-slider" role="img" aria-label="Black and white photo of musicians and dancers in a park under blossoming trees"></section>

  <nav class="site-nav">
    <a class="site-nav__link" href="#">Our mission</a>
    <a class="site-nav__link" href="#">Write for us</a>
    <a class="site-nav__link" href="#">About</a>
    <a class="site-nav__link" href="#">Donate</a>
    <a class="site-nav__link" href="#">Sign up</a>
    <a class="site-nav__link" href="#">Contact</a>
    <span class="site-nav__search">Search Evening Lantern</span>
  </nav>

  <div class="site-brand">
    <span class="site-brand__mark"></span>
    <span class="site-brand__name">The Evening Lantern</span>
  </div>

  <div class="slide-panel"></div>
  <h2 class="slide-headline">Maren Holloway: Spare a thought for the hippies. Their free love revolution is now regulated by a state clipboard</h2>

  <svg class="slide-arrows" width="80" height="16" viewBox="0 0 80 16" aria-label="Previous and next">
    <g fill="none" stroke="#ffffff" stroke-width="1.6">
      <path d="M2 8 H36 M2 8 L9 2 M2 8 L9 14"/>
      <path d="M42 8 H76 M76 8 L69 2 M76 8 L69 14"/>
    </g>
  </svg>
</div>
</body>
</html>
```